Business Card Design needed for logo design project

This project is linked to Consulting Firm + Meeting Space needs logo and bus card..
Our company needs a Business Card Design. Please refer to our original project in the link above.
Industry/Entity Type
Business

```html
<!DOCTYPE html>
<html lang="en">
<head>
<meta charset="utf-8">
<title>Roomnine Business Card</title>
<link rel="stylesheet" href="https://fonts.googleapis.com/css2?family=Exo+2:wght@300;500&display=swap">
<style>
  :root {
    --page-bg: #e9eaec;
    --card-white: #ffffff;
    --brand-blue: #2a78c8;
    --deep-blue: #1f4fb0;
    --light-blue: #5a8fe0;
    --icon-grey: #8d93a8;
    --pattern-tone: #eef0f6;
    --pattern-tone-2: #dde2ee;
  }
  * { box-sizing: border-box; margin: 0; padding: 0; }
  html, body { width: 1200px; height: 900px; overflow: hidden; }
  body {
    background: var(--page-bg);
    font-family: "Exo 2", sans-serif;
    position: relative;
  }
  .card {
    position: absolute;
    left: 250px;
    width: 700px;
    height: 400px;
    background: var(--card-white);
    box-shadow: 0 6px 18px rgba(0,0,0,0.12);
    overflow: hidden;
  }
  .card--back { top: 30px; }
  .card--front { top: 470px; }

  .back-pattern {
    position: absolute;
    inset: 0;
    background: radial-gradient(circle at 50% 50%, var(--pattern-tone) 0%, var(--pattern-tone-2) 100%);
  }
  .brand-name {
    position: absolute;
    color: var(--brand-blue);
    font-weight: 300;
    line-height: 1;
    display: flex;
    align-items: center;
    gap: 10px;
  }
  .brand-dot {
    width: 0.55em;
    height: 0.55em;
    border-radius: 50%;
    background: var(--brand-blue);
  }
  .card--back .brand-name {
    left: 50%;
    top: 50%;
    transform: translate(-50%, -50%);
    font-size: 96px;
  }
  .card--front .brand-name {
    left: 48px;
    top: 38px;
    font-size: 72px;
  }

  .holder { position: absolute; left: 52px; top: 140px; color: var(--deep-blue); }
  .holder-name { font-size: 30px; font-weight: 500; line-height: 1.1; }
  .holder-title { font-size: 24px; font-weight: 500; line-height: 1.1; }

  .address {
    position: absolute; left: 52px; top: 228px;
    color: var(--brand-blue); font-size: 20px; font-weight: 300; line-height: 1.25;
  }

  .contacts {
    position: absolute; left: 52px; top: 298px;
    list-style: none; color: var(--brand-blue); font-size: 21px; font-weight: 300;
  }
  .contacts li { display: flex; align-items: center; gap: 12px; height: 28px; }
  .contacts svg { width: 20px; height: 20px; flex: none; }

  .swoosh { position: absolute; right: 0; bottom: 0; width: 700px; height: 400px; }
</style>
</head>
<body>
  <section class="card card--back">
    <div class="back-pattern" role="img" aria-label="Faint repeating brand-mark pattern across the card back"></div>
    <div class="brand-name"><span>Roomnine</span><span class="brand-dot"></span></div>
  </section>

  <section class="card card--front">
    <div class="brand-name"><span>Roomnine</span><span class="brand-dot"></span></div>

    <div class="holder">
      <p class="holder-name">Daniel Reyes</p>
      <p class="holder-title">President</p>
    </div>

    <p class="address">P.O. Box 4 Lane 18<br>Milford CT</p>

    <ul class="contacts">
      <li>
        <svg viewBox="0 0 20 20" aria-hidden="true"><circle cx="10" cy="10" r="9" fill="none" stroke="var(--icon-grey)" stroke-width="1.5"/><rect x="6.5" y="5" width="7" height="10" rx="1.5" fill="none" stroke="var(--icon-grey)" stroke-width="1.4"/></svg>
        <span>555 0142 678</span>
      </li>
      <li>
        <svg viewBox="0 0 20 20" aria-hidden="true"><circle cx="10" cy="10" r="9" fill="none" stroke="var(--icon-grey)" stroke-width="1.5"/><rect x="5" y="6.5" width="10" height="7" fill="none" stroke="var(--icon-grey)" stroke-width="1.3"/><path d="M5 6.5 L10 10.5 L15 6.5" fill="none" stroke="var(--icon-grey)" stroke-width="1.3"/></svg>
        <span>info@roomnine.com</span>
      </li>
      <li>
        <svg viewBox="0 0 20 20" aria-hidden="true"><circle cx="10" cy="10" r="9" fill="none" stroke="var(--icon-grey)" stroke-width="1.5"/><circle cx="10" cy="10" r="5" fill="none" stroke="var(--icon-grey)" stroke-width="1.3"/><path d="M5 10 H15 M10 5 C7.5 8 7.5 12 10 15 M10 5 C12.5 8 12.5 12 10 15" fill="none" stroke="var(--icon-grey)" stroke-width="1"/></svg>
        <span>www.roomnine.com</span>
      </li>
    </ul>

    <svg class="swoosh" viewBox="0 0 700 400" aria-hidden="true">
      <defs>
        <linearGradient id="swooshBlue" x1="0" y1="1" x2="1" y2="0">
          <stop offset="0" stop-color="#8fb4ef"/>
          <stop offset="0.5" stop-color="var(--light-blue)"/>
          <stop offset="1" stop-color="var(--deep-blue)"/>
        </linearGradient>
      </defs>
      <path d="M250 400 C420 360 560 300 700 190 L700 400 Z" fill="#c9dbf6"/>
      <path d="M310 400 C460 370 590 310 700 215 L700 400 Z" fill="url(#swooshBlue)"/>
      <path d="M330 400 C480 375 600 320 700 245 L700 400 Z" fill="#ffffff" opacity="0.35"/>
    </svg>
  </section>
</body>
</html>
```